Standardization and redesign of graphics for a non-fiction book

For a book project, 11 graphics need to be visually unified so that all the graphics in the book are in the same style. The graphics must be created from scratch. Just new colors aren't enough. Some of the existing graphics are by other authors who own the copyright. Accordingly, the new graphics must be truly new. This is especially true for the "2 S-curves" graphic.

Target Market(s)

Manager Furniture Industry

Industry/Entity Type

Möbel

Colors
0054AA
0677BA
7BADD7
CADEEF
E8F1F8

```html
<!DOCTYPE html>
<html lang="de">
<head>
<meta charset="utf-8">
<title>Grafiken Möbelmarkt</title>
<link href="https://fonts.googleapis.com/css2?family=Source+Sans+3:wght@700;900&display=swap" rel="stylesheet">
<style>
  :root {
    --navy: #1F56A0;
    --blue: #3A8EE0;
    --blue-mid: #2F7FD6;
    --sky: #85D0FA;
    --sky-pale: #B8E6F8;
    --panel: #F3F9FD;
    --ink: #0A0A0A;
    --white: #FFFFFF;
  }
  html, body {
    margin: 0;
    padding: 0;
    width: 1200px;
    height: 566px;
    overflow: hidden;
    background: var(--white);
    font-family: "Source Sans 3", "Source Sans Pro", sans-serif;
  }
  .sheet {
    position: relative;
    width: 1200px;
    height: 566px;
  }
  .graphic {
    position: absolute;
    width: 368px;
    height: 240px;
    background: var(--panel);
    box-shadow: 0 2px 10px rgba(40, 70, 90, 0.22);
  }
  .graphic svg { display: block; width: 368px; height: 240px; }
  .col-1 { left: 30px; }
  .col-2 { left: 413px; }
  .col-3 { left: 801px; }
  .row-1 { top: 34px; }
  .row-2 { top: 292px; }

  text { font-family: "Source Sans 3", "Source Sans Pro", sans-serif; font-weight: 900; text-anchor: middle; }
  .title { fill: var(--ink); font-size: 15px; letter-spacing: 0.2px; }
  .title-lg { fill: var(--ink); font-size: 16px; letter-spacing: 0.3px; }
  .label-white { fill: var(--white); }
  .label-shadow { fill: var(--white); filter: drop-shadow(0.6px 0.8px 0.4px rgba(20, 50, 90, 0.6)); }
  .step-label { fill: var(--ink); font-size: 8.5px; font-weight: 700; }
  .connector { fill: none; stroke: var(--blue); stroke-width: 2.6; stroke-linecap: round; stroke-linejoin: round; }
</style>
</head>
<body>
<main class="sheet">

  <!-- Einflussfaktoren -->
  <section class="graphic col-1 row-1" aria-label="Einflussfaktoren Möbelmarkt">
    <svg viewBox="0 0 368 240">
      <rect x="109" y="48" width="150" height="53.5" rx="11" fill="var(--navy)"/>
      <text class="label-white" x="184" y="72" font-size="13">EINFLUSSFAKTOREN</text>
      <text class="label-white" x="184" y="87" font-size="13">MÖBELMARK</text>
      <path class="connector" d="M184 108.5 V143 M109.5 142 V126 H258.5 V142"/>
      <path class="connector" d="M102.5 137 L109.5 144 L116.5 137 M177 137 L184 144 L191 137 M251.5 137 L258.5 144 L265.5 137"/>
      <rect x="68.5" y="154.7" width="82" height="37.7" rx="8" fill="var(--sky)"/>
      <rect x="159" y="154.7" width="50" height="37.7" rx="8" fill="var(--navy)"/>
      <rect x="217.5" y="154.7" width="82" height="37.7" rx="8" fill="var(--sky)"/>
      <text class="label-shadow" x="109.5" y="177.3" font-size="10.5">WIRTSCHAFT</text>
      <text class="label-white" x="184" y="177.3" font-size="10.5">TRENDS</text>
      <text class="label-shadow" x="258.5" y="177.3" font-size="10.5">KUNDEN</text>
    </svg>
  </section>

  <!-- Beratungsangebote -->
  <section class="graphic col-2 row-1" aria-label="Beratungsangebote">
    <svg viewBox="0 0 368 240">
      <rect x="88" y="62" width="74" height="95" rx="6" fill="var(--navy)" role="img" aria-label="Figur eines Beraters, der auf die Tafel zeigt"/>
      <rect x="164.5" y="56" width="114" height="82" fill="none" stroke="var(--navy)" stroke-width="3"/>
      <rect x="194.7" y="101.5" width="14.9" height="16.4" rx="1.5" fill="var(--blue-mid)"/>
      <rect x="219" y="87.6" width="16" height="30.3" rx="2" fill="var(--sky)"/>
      <rect x="243.6" y="69.9" width="16.4" height="48" rx="2" fill="var(--sky-pale)"/>
      <line x1="188" y1="120" x2="267" y2="120" stroke="var(--navy)" stroke-width="3" stroke-linecap="round"/>
      <text class="title-lg" x="184" y="180">BERATUNGSANGEBOTE</text>
    </svg>
  </section>

  <!-- Customer Journey -->
  <section class="graphic col-3 row-1" aria-label="Customer Journey">
    <svg viewBox="0 0 368 240">
      <text class="title" x="184" y="78">CUSTOMER JOUNRNEY</text>
      <g fill="var(--blue)" stroke="var(--blue-mid)" stroke-width="0.8">
        <circle cx="56.8" cy="129.5" r="18"/>
        <circle cx="117.4" cy="129.5" r="18"/>
        <circle cx="177.9" cy="129.5" r="18"/>
        <circle cx="238.5" cy="129.5" r="18"/>
        <circle cx="299" cy="129.5" r="18"/>
      </g>
      <g fill="none" stroke="var(--blue)" stroke-width="1.8" stroke-linecap="round" stroke-linejoin="round">
        <path d="M75 129.5 H89 M85 125.5 L89 129.5 L85 133.5"/>
        <path d="M135.6 129.5 H149.6 M145.6 125.5 L149.6 129.5 L145.6 133.5"/>
        <path d="M196.1 129.5 H210.1 M206.1 125.5 L210.1 129.5 L206.1 133.5"/>
        <path d="M256.7 129.5 H270.7 M266.7 125.5 L270.7 129.5 L266.7 133.5"/>
        <path d="M317.2 129.5 H331.2 M327.2 125.5 L331.2 129.5 L327.2 133.5"/>
      </g>
      <text class="step-label" x="56.8" y="173">Awareness</text>
      <text class="step-label" x="117.4" y="173">Consideration</text>
      <text class="step-label" x="177.9" y="173">Purchase</text>
      <text class="step-label" x="238.5" y="173">Retention</text>
      <text class="step-label" x="299" y="173">Loallty</text>
    </svg>
  </section>

  <!-- Entwicklung Möbelmarkt -->
  <section class="graphic col-1 row-2" aria-label="Entwicklung deutscher Möbelmarkt">
    <svg viewBox="0 0 368 240">
      <text class="title" x="184" y="44">ENTWICKLUNG DEUTSCHER</text>
      <text class="title" x="184" y="59">MÖBELMARKT</text>
      <polygon fill="var(--sky-pale)" points="83.8,190.5 130.4,154.6 138.3,159.3 153.7,146.3 173.7,158.4 212.9,120.2 228.2,130 237.6,122.5 244.5,125.3 270.2,102 270.2,190.5"/>
      <polyline fill="none" stroke="var(--blue)" stroke-width="2.6" stroke-linejoin="round" stroke-linecap="round" points="89.9,182.6 130.4,157.4 138.3,162 153.7,149 173.7,161.2 212.9,123 228.2,132.8 237.6,125.3 244.5,128.1 274.8,95"/>
      <path d="M265 96.5 L274.8 95 L273.5 105" fill="none" stroke="var(--blue)" stroke-width="2.6" stroke-linecap="round" stroke-linejoin="round"/>
      <path d="M76.4 81.5 V195.6 H294.4" fill="none" stroke="var(--blue)" stroke-width="5.5" stroke-linecap="round" stroke-linejoin="miter"/>
    </svg>
  </section>

  <!-- Relevante Megatrends -->
  <section class="graphic col-2 row-2" aria-label="Relevante Megatrends">
    <svg viewBox="0 0 368 240">
      <circle cx="184.5" cy="130" r="74.5" fill="none" stroke="var(--navy)" stroke-width="3"/>
      <circle cx="184.5" cy="130" r="38" fill="var(--navy)"/>
      <text class="label-white" x="184.5" y="128" font-size="9.5">RELEVANTE</text>
      <text class="label-white" x="184.5" y="138.5" font-size="9.5">MEGATRENDS</text>
      <g fill="var(--sky)">
        <circle cx="184.5" cy="56.8" r="25"/>
        <circle cx="253" cy="104.3" r="25"/>
        <circle cx="234.3" cy="183.5" r="25"/>
        <circle cx="130.9" cy="180.3" r="25"/>
        <circle cx="115.5" cy="104.3" r="25"/>
      </g>
      <g font-size="11">
        <text class="label-shadow" x="184.5" y="60.5">Trend</text>
        <text class="label-shadow" x="253" y="108">Trend</text>
        <text class="label-shadow" x="234.3" y="187.2">Trend</text>
        <text class="label-shadow" x="130.9" y="184">Trend</text>
        <text class="label-shadow" x="115.5" y="108">Trend</text>
      </g>
    </svg>
  </section>

  <!-- Qualitätspyramide -->
  <section class="graphic col-3 row-2" aria-label="Qualitätspyramide Nachhaltigkeit">
    <svg viewBox="0 0 368 240">
      <text class="title" x="184" y="43">QUALITÄTSPYRAMIDE</text>
      <text class="title" x="184" y="59">NACHHALTIGKEIT</text>
      <polygon fill="var(--sky)" points="184,81 208.7,112.7 159.3,112.7"/>
      <polygon fill="var(--blue)" points="156,116 212,116 233,144.9 135,144.9"/>
      <polygon fill="var(--blue-mid)" points="131.8,148 236.6,148 257.1,176.5 110.9,176.5"/>
      <polygon fill="var(--navy)" stroke="var(--navy)" stroke-width="2" stroke-linejoin="round" points="107.1,179.8 260.9,179.8 281.8,210.5 86.2,210.5"/>
      <text class="label-white" x="184" y="106.5" font-size="5.5">LIFESPAN</text>
      <text class="label-white" x="184" y="135.2" font-size="9.5">DISTRIBUTION</text>
      <text class="label-white" x="184" y="168.5" font-size="13">MANUFACTURING</text>
      <text class="label-white" x="184" y="203.5" font-size="17">DESIGN</text>
    </svg>
  </section>

</main>
</body>
</html>
```